New Business Card Design Project - RK Ledgerwise & Filing Partners, LLC

Below is a sample image of the card (TM Bookkeeping). I would like to have a designed business card that looks very similar (Front & Back). In addition, I would like to keep the same colors as well. I attached my Business Logo (RK Ledgerwise & Filing Partners, LLC) that will be on my website.

Target Market(s)

Executives, Business Owners, Board of Directors, Chief Financial Officers

Contact Information for Business Card

Font styles to use
Serif

Colors
0c5ba6
ffffff
5c5c5c

Requirements
Must have
• My Name: Malcolm Ferris, CPA
• Position: Owner
• Phone: (240) 555-0148
• Email: Mferris@rkledgerwise.example
• Website: www.Rkledgerwise.example
• Address: 4736 Ferncliff Ave #2093
• Dunmore Falls, MD 21990
Nice to have
• Same design & color scheme as TM Bookkeepnig Business card sample attached

```html
<!DOCTYPE html>
<html lang="en">
<head>
<meta charset="utf-8">
<title>RK Ledgerwise &amp; Filing Partners, LLC — Business Card</title>
<link rel="stylesheet" href="https://fonts.googleapis.com/css2?family=Crimson+Pro:wght@400;500&display=swap">
<style>
  :root {
    --brand-blue: #0c5ba6;
    --paper: #ffffff;
    --ink-grey: #5c5c5c;
    --ink-dark: #3a3a3a;
    --backdrop: #e6e7ea;
    --serif: "Crimson Pro", "Times New Roman", serif;
  }
  * { box-sizing: border-box; margin: 0; padding: 0; }
  html, body {
    width: 1200px; height: 800px; overflow: hidden;
    background: var(--backdrop);
    font-family: var(--serif);
  }
  .canvas { position: relative; width: 1200px; height: 800px; }

  .card {
    position: absolute;
    width: 560px; height: 320px;
    left: 320px;
    overflow: hidden;
    box-shadow: 0 10px 28px rgba(0,0,0,.18);
  }
  .card--front { top: 50px; background: var(--brand-blue); }
  .card--back  { top: 420px; background: var(--paper); }

  /* Front */
  .front-name {
    position: absolute; inset: 0;
    display: flex; align-items: center; justify-content: center;
    text-align: center;
    color: var(--paper);
    font-weight: 400;
    font-size: 27px;
    letter-spacing: 1.5px;
    line-height: 1.25;
  }

  /* Back */
  .back-name {
    position: absolute; left: 40px; top: 130px; width: 210px;
    color: var(--brand-blue);
    font-weight: 400;
    font-size: 19px;
    letter-spacing: 1px;
    line-height: 1.25;
    text-align: center;
  }
  .divider {
    position: absolute; left: 272px; top: 82px;
    width: 1px; height: 118px;
    background: var(--brand-blue);
  }
  .contact {
    position: absolute; left: 296px; top: 74px;
    color: var(--ink-dark);
    font-size: 14px; line-height: 1.3;
  }
  .contact__name { font-size: 17px; }
  .contact__role { color: var(--brand-blue); font-size: 15px; margin-bottom: 10px; }
  .contact__row { display: flex; align-items: center; gap: 7px; }
  .contact__row svg { width: 11px; height: 11px; fill: var(--brand-blue); flex: none; }
  .contact__address { padding-left: 18px; }

  .bands { position: absolute; left: 0; bottom: 0; width: 560px; height: 60px; }
  .website {
    position: absolute; right: 22px; bottom: 10px;
    color: var(--paper); font-size: 13px; letter-spacing: .3px;
  }
</style>
</head>
<body>
<main class="canvas">

  <section class="card card--front" aria-label="Card front">
    <p class="front-name">RK LEDGERWISE<br>&amp; FILING PARTNERS, LLC</p>
  </section>

  <section class="card card--back" aria-label="Card back">
    <p class="back-name">RK LEDGERWISE<br>&amp; FILING PARTNERS, LLC</p>

    <div class="divider"></div>

    <div class="contact">
      <p class="contact__name">Malcolm Ferris, CPA</p>
      <p class="contact__role">Owner</p>
      <p class="contact__row">
        <svg viewBox="0 0 24 24" aria-hidden="true"><path d="M6.6 10.8a15 15 0 0 0 6.6 6.6l2.2-2.2c.3-.3.7-.4 1-.2 1.1.4 2.3.6 3.6.6.6 0 1 .4 1 1V20c0 .6-.4 1-1 1A17 17 0 0 1 3 4c0-.6.4-1 1-1h3.5c.6 0 1 .4 1 1 0 1.3.2 2.5.6 3.6.1.3 0 .7-.2 1z"/></svg>
        (240) 555-0148
      </p>
      <p class="contact__row">
        <svg viewBox="0 0 24 24" aria-hidden="true"><path d="M2 5h20v14H2z M2 5l10 8 10-8" stroke="#fff" stroke-width="1.6"/></svg>
        Mferris@rkledgerwise.example
      </p>
      <p class="contact__address">4736 Ferncliff Ave #2093<br>Dunmore Falls, MD 21990</p>
    </div>

    <svg class="bands" viewBox="0 0 560 60" aria-hidden="true">
      <path d="M0 48 L368 48 L378 36 L560 36" fill="none" stroke="var(--ink-grey)" stroke-width="5"/>
      <path d="M0 52 L370 52 L382 40 Q384 38 388 38 L560 38 L560 60 L0 60 Z" fill="var(--brand-blue)"/>
    </svg>
    <p class="website">www.Rkledgerwise.example</p>
  </section>

</main>
</body>
</html>
```